Bright Loom Allies, LLC
Collaborative Contract Solutions
Modern
Owen Darby
Managing Director
12 Juniper Vale Road
Suite 240
Calderwood, NH 01847
owen@brightloomallies.com
www.brightloomallies.com
Docs said to upload this logo format.

```html
<!DOCTYPE html>
<html lang="en">
<head>
<meta charset="utf-8">
<title>Bright Loom Allies, LLC — Business Card</title>
<link rel="stylesheet" href="https://fonts.googleapis.com/css2?family=Arimo:wght@400;700&display=swap">
<style>
  :root {
    --stage: #3a2a20;
    --card-light: #efefef;
    --card-mid: #dcdcdc;
    --card-dark: #c4c4c4;
    --brand-blue: #1f7fc4;
    --brand-blue-deep: #0f4f94;
    --brand-blue-light: #6fb4e6;
    --name-grey: #4d4d4d;
    --text-grey: #3c3c3c;
    --bullet: #e9a21a;
  }
  * { box-sizing: border-box; margin: 0; padding: 0; }
  html, body {
    width: 1200px; height: 850px; overflow: hidden;
    background: var(--stage);
  }
  .canvas { position: relative; width: 1200px; height: 850px; }
  .business-card {
    position: absolute; left: 150px; top: 152px;
    width: 900px; height: 545px;
    border-radius: 10px; overflow: hidden;
    background: linear-gradient(160deg, var(--card-light) 0%, var(--card-mid) 55%, var(--card-dark) 100%);
    box-shadow: 0 6px 18px rgba(0,0,0,0.45);
    font-family: "Arimo", sans-serif;
  }
  .corner-swoosh { position: absolute; inset: 0; width: 900px; height: 545px; }
  .brand {
    position: absolute; left: 0; right: 0; top: 44px;
    display: flex; flex-direction: column; align-items: center;
    padding-left: 60px;
  }
  .brand-dot {
    width: 110px; height: 110px; border-radius: 50%;
    background: var(--brand-blue);
    margin-bottom: 20px;
  }
  .brand-name {
    font-weight: 700; font-size: 40px; letter-spacing: -0.5px;
    color: var(--brand-blue);
  }
  .name-plate {
    position: absolute; left: 320px; top: 276px;
    width: 424px; height: 80px; border-radius: 8px;
    background: linear-gradient(180deg, #d3d3d3 0%, #ececec 100%);
    border: 1px solid #b9b9b9;
    display: flex; align-items: center; justify-content: center;
    font-size: 50px; color: var(--name-grey); letter-spacing: 0.5px;
  }
  .contact-list {
    position: absolute; left: 56px; top: 374px;
    list-style: none; font-size: 20px; color: var(--text-grey);
    line-height: 29px;
  }
  .contact-item { display: flex; align-items: center; gap: 12px; }
  .contact-item.continued { padding-left: 30px; }
  .contact-icon { width: 18px; height: 18px; flex: none; }
</style>
</head>
<body>
<main class="canvas">
  <section class="business-card">
    <svg class="corner-swoosh" viewBox="0 0 900 545" aria-hidden="true">
      <defs>
        <linearGradient id="swooshTop" x1="0" y1="0" x2="1" y2="1">
          <stop offset="0" stop-color="var(--brand-blue-deep)"/>
          <stop offset="1" stop-color="var(--brand-blue)"/>
        </linearGradient>
        <linearGradient id="swooshBottom" x1="1" y1="1" x2="0" y2="0">
          <stop offset="0" stop-color="var(--brand-blue-deep)"/>
          <stop offset="1" stop-color="var(--brand-blue)"/>
        </linearGradient>
      </defs>
      <path d="M0,0 H175 C120,14 52,50 28,130 C14,190 12,330 10,470 H0 Z" fill="url(#swooshTop)"/>
      <path d="M175,0 C120,14 52,50 28,130 C14,190 12,330 10,470" fill="none" stroke="var(--brand-blue-light)" stroke-width="4"/>
      <path d="M900,545 H690 C760,536 834,500 866,420 C884,360 888,200 890,70 H900 Z" fill="url(#swooshBottom)"/>
      <path d="M690,545 C760,536 834,500 866,420 C884,360 888,200 890,70" fill="none" stroke="var(--brand-blue-light)" stroke-width="4"/>
    </svg>

    <header class="brand">
      <div class="brand-dot"></div>
      <div class="brand-name">Bright Loom Allies</div>
    </header>

    <div class="name-plate">Owen Darby</div>

    <ul class="contact-list">
      <li class="contact-item">
        <svg class="contact-icon" viewBox="0 0 18 18" aria-hidden="true"><circle cx="9" cy="9" r="9" fill="var(--bullet)"/><path d="M6,4.5 l2,2 -1,1.2 c0.8,1.5 1.6,2.3 3.1,3.1 l1.2,-1 2,2 -1.3,1.4 c-3.5,-0.6 -6.4,-3.5 -7,-7 z" fill="#fff"/></svg>
        <span>555.013.4421</span>
      </li>
      <li class="contact-item">
        <svg class="contact-icon" viewBox="0 0 18 18" aria-hidden="true"><circle cx="9" cy="9" r="9" fill="var(--bullet)"/><circle cx="9" cy="9" r="4.5" fill="none" stroke="#fff" stroke-width="1.4"/><path d="M4.5,9 H13.5 M9,4.5 V13.5" stroke="#fff" stroke-width="1.2"/></svg>
        <span>www.brightloomallies.com</span>
      </li>
      <li class="contact-item">
        <svg class="contact-icon" viewBox="0 0 18 18" aria-hidden="true"><circle cx="9" cy="9" r="9" fill="var(--bullet)"/><rect x="4.5" y="6" width="9" height="6.5" fill="none" stroke="#fff" stroke-width="1.3"/><path d="M4.5,6 L9,9.8 13.5,6" fill="none" stroke="#fff" stroke-width="1.3"/></svg>
        <span>owen@brightloomallies.com</span>
      </li>
      <li class="contact-item">
        <svg class="contact-icon" viewBox="0 0 18 18" aria-hidden="true"><circle cx="9" cy="9" r="9" fill="var(--bullet)"/><path d="M9,14 C6.5,10.5 5.8,9.4 5.8,7.6 a3.2,3.2 0 0 1 6.4,0 c0,1.8 -0.7,2.9 -3.2,6.4 z" fill="#fff"/><circle cx="9" cy="7.6" r="1.2" fill="var(--bullet)"/></svg>
        <span>12 Juniper Vale Road Suite 240</span>
      </li>
      <li class="contact-item continued"><span>Calderwood, NH 01847</span></li>
    </ul>
  </section>
</main>
</body>
</html>
```